Deliver a professional and engaging investment propsal.

I am appealing to highend smart investors and need a high quality, engaging and formal presentation in PDF.
StowBin: https://www.stowbin.net/sh/qwmtr48kelvan2x/ZZTrPHmLe7WqsnBFjQ4kR8vYt?dl=0
Text for project is in Stowbin called New Proposal Final
Along with past much older attempts of this job.
Any additional ideas to enable a better outcome would be appreicated.

```html
<!DOCTYPE html>
<html lang="en">
<head>
<meta charset="utf-8">
<title>Investment Proposal – Pages 5 and 6</title>
<link href="https://fonts.googleapis.com/css2?family=Arimo:wght@400;700&family=Cinzel:wght@600;700&family=Nunito:wght@800&display=swap" rel="stylesheet">
<style>
  :root{
    --stage:#000000;
    --paper:#ffffff;
    --violet:#5a12f2;
    --sky:#6cc3ee;
    --navy:#28226b;
    --ink:#111111;
    --link:#7fd0ff;
    --label:#ffffff;
  }
  *{box-sizing:border-box;margin:0;padding:0}
  html,body{width:1200px;height:720px;overflow:hidden;background:var(--stage)}
  .canvas{position:relative;width:1200px;height:720px;font-family:"Arimo",Arial,sans-serif}
  .page{position:absolute;background:var(--paper)}
  .page-five{left:94px;top:26px;width:446px;height:626px}
  .page-six{left:662px;top:33px;width:451px;height:624px}
  .page-label{position:absolute;color:var(--label);font-size:29px;font-family:"Arimo",Arial,sans-serif}
  .label-five{left:96px;top:656px}
  .label-six{left:664px;top:664px}

  .header{position:absolute;left:6px;right:6px;top:6px;height:78px;display:flex}
  .header-title{flex:1;background:var(--violet);color:#fff;font-family:"Cinzel",serif;font-weight:700;
    display:flex;align-items:center;justify-content:center;text-align:center;line-height:1.15}
  .page-five .header-title{font-size:22px;letter-spacing:1px;flex:0 0 327px}
  .page-six .header-title{font-size:25px;letter-spacing:1px;flex:0 0 330px}
  .header-number{flex:1;background:var(--sky);color:var(--navy);font-family:"Nunito",sans-serif;font-weight:800;
    font-size:40px;display:flex;align-items:center;justify-content:center}

  .team-panel{position:absolute;left:6px;right:6px;top:84px;height:535px;background:var(--navy);color:#fff}
  .team-copy{padding:12px 12px 0 12px;font-size:12.6px;line-height:15px}
  .team-copy h3{color:var(--link);font-weight:400;font-size:12.8px}
  .team-copy p{margin-bottom:14px}
  .street-photo{position:absolute;left:0;right:0;top:262px;height:252px;
    background:linear-gradient(180deg,#9fb0c4 0%,#c9cfd6 35%,#8a6f58 60%,#7b7370 100%)}
  .street-photo svg{position:absolute;left:0;bottom:0;width:100%;height:70px}

  .conclusion{position:absolute;left:12px;right:10px;top:92px;color:var(--ink);font-size:12.8px;line-height:13.6px}
  .conclusion h2{font-weight:400;font-size:13px;margin-bottom:13px}
  .conclusion p{margin-bottom:14px}
  .plan-caption{position:absolute;left:0;right:0;top:262px;text-align:center;color:#222;line-height:1.1}
  .plan-caption .kicker{font-size:6.5px;letter-spacing:.5px;text-transform:uppercase;margin-left:-40px}
  .plan-caption .name{font-size:10px;font-weight:700;font-style:italic;letter-spacing:.5px;margin-left:-60px}
  .site-plan{position:absolute;left:40px;top:283px;width:375px;height:175px;
    background:linear-gradient(135deg,#7a9a5c,#a9b39a 40%,#8c9b7a 70%,#6f8f58);border:1px solid #8b8b8b}
  .gallery{position:absolute;top:462px;height:49px}
  .g1{left:30px;width:125px;background:linear-gradient(180deg,#c9d3de,#b8a58c)}
  .g2{left:162px;width:144px;background:linear-gradient(180deg,#8fb3d6,#7a8a56)}
  .g3{left:312px;width:110px;background:linear-gradient(180deg,#9ec2de,#8c4a38)}
  .contact{position:absolute;left:6px;right:6px;top:519px;height:99px;background:var(--navy);color:#fff;text-align:center}
  .contact .intro{font-size:14px;margin-top:2px}
  .contact .person{font-size:17px;font-weight:700;margin-top:14px}
  .contact .line{font-size:14px;line-height:15px}
  .contact a{color:#fff;text-decoration:underline}
</style>
</head>
<body>
<div class="canvas">

  <section class="page page-five">
    <header class="header">
      <h1 class="header-title">About Our<br>Quality Team</h1>
      <div class="header-number">5</div>
    </header>
    <div class="team-panel">
      <div class="team-copy">
        <h3>Owner - Marcus Hale</h3>
        <p>I am an investor always seeking great value opportunities.</p>
        <h3>Our KTR Engineering Design and Planning Team</h3>
        <p>From planning to conceptual design to construction services, our planning department understands the innovative solutions needed for your project needs. Our planners collaborate with other design professions to create innovative solutions for planning projects and other design needs. KTR designs with nature in mind and creating sustainable solutions to each unique and individual design requirement. Our pursuit is to bring the public a service with solid goals and concepts by challenging old convention and implementing new life-giving communities and spaces.<br>We have experience and capabilities in conceptual project development, master planning, feasibility studies, park and recreational design, urban and land planning.</p>
      </div>
      <div class="street-photo" role="img" aria-label="Photo of a small-town main street with shops and parked trucks under a cloudy sky">
        <svg viewBox="0 0 434 70" preserveAspectRatio="none" aria-hidden="true">
          <path d="M0 0 Q217 110 434 0 L434 70 L0 70 Z" fill="#28226b"/>
        </svg>
      </div>
    </div>
  </section>
  <div class="page-label label-five">Page 5</div>

  <section class="page page-six">
    <header class="header">
      <h1 class="header-title">In Conclusion</h1>
      <div class="header-number">6</div>
    </header>
    <div class="conclusion">
      <h2>In Conclusion</h2>
      <p>This is a solid project located in the Bakken on top of the most cost-effective oil reserves anywhere in the Bakken, centrally located for business and with highway frontage and now with the new Bypass intersection at our doorstep, it creates an incredible opportunity.</p>
      <p>I would love to have you come on board as partner, our focus is pushing hard and fast to<br>take advantage of the window of opportunity with the weather in March next year and have everything ready to roll and have lots ready for sale before August 2019.</p>
    </div>
    <div class="plan-caption">
      <div class="kicker">60 Acre Mixed-Use Development</div>
      <div class="name">RIDGELINE TOWN CENTER</div>
    </div>
    <div class="site-plan" role="img" aria-label="Site plan of the 60 acre mixed-use town center with lots, roads, parking and one sold parcel"></div>
    <div class="gallery g1" role="img" aria-label="Rendering of a hotel building marked coming soon"></div>
    <div class="gallery g2" role="img" aria-label="Rendering of a town center plaza with trees"></div>
    <div class="gallery g3" role="img" aria-label="Rendering of brick storefront buildings"></div>
    <div class="contact">
      <div class="intro">Please send all questions and all joint venture proposals to:</div>
      <div class="person">Marcus Hale</div>
      <div class="line">email: <a href="mailto:mrmarcushale@fastpost.net">mrmarcushale@fastpost.net</a></div>
      <div class="line">Australia</div>
      <div class="line">+61 409555218</div>
    </div>
  </section>
  <div class="page-label label-six">Page 6</div>

</div>
</body>
</html>
```